International Luxury Furniture and Accessories Outsourcing Company

We Need a Business Card design for a new Outsourcing company doing Business Internationally in the Luxury Furniture and Accessories Space. The company's name is CORVIN HALDEN and we deal with clients in the high end and Luxury Space for Furniture and Accessories in the world. We would like Designs that speaks Luxury and Professionalism.

We like the Combination of the color Brown and Gold or Black and Gold. We are also open to other color combo.

We like some of the design of file attached.
Updates

This is Marcus and We really appreciate all of you taking the time out and putting the effort to help us jump start our new company. We have 2-3 designs that we like and will decide soon to pick one. Once again, Thank you to all of you !! Best Regards, Marcus

Industry/Entity Type

Business

```html
<!DOCTYPE html>
<html lang="en">
<head>
<meta charset="utf-8">
<title>Corvin Halden — Business Card</title>
<link rel="stylesheet" href="https://fonts.googleapis.com/css2?family=Cinzel:wght@400;500&display=swap">
<style>
  :root {
    --backdrop: #e9e4dc;
    --card-black: #050505;
    --card-sheen: #141414;
    --gold-light: #f6e27a;
    --gold-mid: #d4a52a;
    --gold-deep: #8a6510;
  }
  html, body {
    margin: 0;
    padding: 0;
    width: 1200px;
    height: 900px;
    overflow: hidden;
    background: var(--backdrop);
  }
  .canvas {
    position: relative;
    width: 1200px;
    height: 900px;
    display: flex;
    align-items: center;
    justify-content: center;
  }
  .business-card {
    position: relative;
    width: 840px;
    height: 480px;
    background: var(--card-black);
    overflow: hidden;
    box-shadow: 0 18px 40px rgba(0, 0, 0, 0.25);
  }
  .card-texture {
    position: absolute;
    inset: 0;
    background: radial-gradient(ellipse at 50% 40%, var(--card-sheen) 0%, var(--card-black) 70%);
  }
  .brand-block {
    position: absolute;
    left: 0;
    right: 0;
    top: 196px;
    text-align: center;
  }
  .brand-name,
  .brand-reflection {
    font-family: "Cinzel", serif;
    font-weight: 500;
    font-size: 44px;
    letter-spacing: 2px;
    line-height: 1.1;
    margin: 0;
    background: linear-gradient(180deg, var(--gold-light) 0%, var(--gold-mid) 55%, var(--gold-deep) 100%);
    -webkit-background-clip: text;
    background-clip: text;
    color: transparent;
  }
  .initial {
    font-size: 60px;
  }
  .brand-reflection {
    transform: scaleY(-1);
    opacity: 0.22;
    margin-top: 0;
    -webkit-mask-image: linear-gradient(0deg, #000 0%, transparent 55%);
    mask-image: linear-gradient(0deg, #000 0%, transparent 55%);
  }
</style>
</head>
<body>
  <main class="canvas">
    <section class="business-card">
      <div class="card-texture" role="img" aria-label="Faint dark lattice pattern covering the card background"></div>
      <div class="brand-block">
        <h1 class="brand-name"><span class="initial">C</span>ORVIN <span class="initial">H</span>ALDEN</h1>
        <div class="brand-reflection" aria-hidden="true"><span class="initial">C</span>ORVIN <span class="initial">H</span>ALDEN</div>
      </div>
    </section>
  </main>
</body>
</html>
```